Bright and beautiful business card for a coach

I'm a personal and business coach based in Perth, Australia. I need a business card that whilst subtle and elegant, will stand out and appeal on a table full of cards.

My business name is Tide Mentoring and the business card must represent the warmth and brightness implied in the name, without being gimmicky. It must have a warmth and appeal and be easy to read.

I prefer clean, minimalist designs.

It must align with the feel of my website and socials: https://www.tidementoring.com.au/
https://www.instagram.com/tidementoringau/
https://www.facebook.com/tidementoringau
Updates

Hi Designers Thank you so much for taking the time to submit designs. I wonder if I could have explained myself a little better. Most of the designs that have been submitted look rather formal and many have quite corporate looking embellishments on them (to my eye). I would like softer, warmer, more organic. I’m open to people playing about and being more abstract, using softer embellishments (e.g the line drawing flowers and grasses I’ve used in my socials) incorporating other colours from my palette or like the social icons in my email signature (in PDF), perhaps playing with size/oversize, playing with the bleed. Please don’t be constrained by what I’ve already done, it merely needs to compliment. I’m sorry if I’m not using the right words or have led you astray. I’m no designer, but I’ve done my website, socials, email signature etc all myself (my logo was a design contest) and I was really hoping for my business card to be something more creative than I could have made with a template. Reminder: No black cards/sides please. Thank you 😊

Target Market(s)

Individuals, most likely but not all female. Creative thinkers. Likely professionals.

Industry/Entity Type

Business & Personal Coach

Contact Information for Business Card

(Tide Mentoring Logo) Name: Maren Delsby; Title: Business & Personal Coach; Phone number: +61 (0)438 915307; Email: maren@tidementoring.com.au; Website: https://tidementoring.com.au; Social icons for Facebook, Instagram & LinkedIn: @tidementoringAU. Optional strapline: "A thinking partner to help you cut through the noise"

Font styles to use
Sans Serif

Colors
00AB8E
00BBA5
67D7C9
C6EFE9
E9F9F6
59FF00
82FF00
B8FF75
E3FFCB
F4FFEA
FFC000
F8CF3A
FAE287
FDF2CF
FEFAEE

Requirements
Must have
• Must align with feel of my website and socials. Must have a pop of #FFC000 (possibly whole of one side, or at least a block). Bright or white background. Easy to read.
Nice to have
• Possibly incorporate the sunshine/grass picture I have used in website and socials - will upload.
Should not have
• Must not be black or dark. Not impersonal or corporate looking.

```html
<!DOCTYPE html>
<html lang="en">
<head>
<meta charset="utf-8">
<title>Tide Mentoring – Business Card</title>
<link rel="stylesheet" href="https://fonts.googleapis.com/css2?family=Montserrat:wght@400;700&family=Roboto:wght@400&display=swap">
<style>
  :root {
    --bg: #ecebe8;
    --card-white: #ffffff;
    --amber: #c8731c;
    --amber-deep: #b5651a;
    --gold: #f3b21f;
    --ink: #3a3a3a;
    --ink-soft: #555555;
    --grey-logo: #8a8a8a;
    --grass-dark: #3f6b1a;
    --grass: #7fb33a;
    --sun: #f6e3c4;
  }
  * { margin: 0; padding: 0; box-sizing: border-box; }
  html, body { width: 1200px; height: 900px; overflow: hidden; }
  body {
    background: var(--bg);
    font-family: "Roboto", Arial, sans-serif;
    color: var(--ink);
    position: relative;
  }
  .card {
    position: absolute;
    left: 250px;
    width: 700px;
    height: 400px;
    border-radius: 22px;
    overflow: hidden;
    box-shadow: 0 6px 18px rgba(0,0,0,0.12);
  }
  .card--front { top: 30px; background: var(--card-white); }
  .card--back { top: 470px; }

  .front__edge {
    position: absolute; left: 0; right: 0; bottom: 0; height: 10px;
    background: linear-gradient(90deg, var(--amber), var(--gold));
  }
  .brand {
    position: absolute;
    font-family: "Montserrat", Arial, sans-serif;
    font-weight: 400;
    letter-spacing: 6px;
    text-transform: uppercase;
    display: flex; align-items: center; gap: 14px;
  }
  .brand__dot { width: 16px; height: 16px; border-radius: 50%; display: inline-block; }
  .front__brand { top: 80px; left: 330px; font-size: 26px; color: var(--amber); }
  .front__brand .brand__dot { background: var(--gold); }

  .person { position: absolute; left: 50px; top: 200px; }
  .person__name {
    font-family: "Montserrat", Arial, sans-serif;
    font-weight: 700; font-size: 30px; color: var(--amber);
    letter-spacing: 1px; text-transform: uppercase;
  }
  .person__title { font-size: 17px; color: var(--ink-soft); margin-top: 2px; }

  .divider {
    position: absolute; left: 360px; top: 195px; width: 2px; height: 100px;
    background: var(--amber);
  }
  .contacts { position: absolute; left: 385px; top: 196px; list-style: none; }
  .contacts li {
    display: flex; align-items: center; gap: 9px;
    font-size: 16px; color: var(--ink); line-height: 25px;
  }
  .contacts svg { width: 15px; height: 15px; flex: none; }
  .social-dots { display: flex; gap: 3px; }
  .social-dots span { width: 13px; height: 13px; border-radius: 50%; background: var(--amber); }

  .strapline {
    position: absolute; left: 50px; top: 335px;
    font-size: 17px; color: var(--ink-soft);
  }

  .back__photo {
    position: absolute; inset: 0;
    background:
      radial-gradient(circle at 78% 22%, var(--sun) 0%, rgba(246,227,196,0.6) 14%, rgba(246,227,196,0) 38%),
      linear-gradient(170deg, #9bc35a 0%, var(--grass) 40%, var(--grass-dark) 100%);
  }
  .back__brand { top: 170px; left: 190px; font-size: 34px; color: #ffffff; }
  .back__brand .brand__dot { background: #ffffff; }
</style>
</head>
<body>
  <section class="card card--front" aria-label="Card front">
    <div class="brand front__brand"><span class="brand__dot"></span>Tide Mentoring</div>

    <div class="person">
      <h1 class="person__name">Maren Delsby</h1>
      <p class="person__title">Business &amp; Personal Coach</p>
    </div>

    <div class="divider"></div>

    <ul class="contacts">
      <li>
        <svg viewBox="0 0 16 16"><path fill="#c8731c" d="M3 1.5l2.5 0 1 3.5-1.7 1.2a8 8 0 0 0 5 5l1.2-1.7 3.5 1v2.5c0 .8-.7 1.5-1.5 1.5A12.5 12.5 0 0 1 1.5 3c0-.8.7-1.5 1.5-1.5z"/></svg>
        +61 (0)438 915307
      </li>
      <li>
        <svg viewBox="0 0 16 16"><rect x="1" y="3" width="14" height="10" rx="1" fill="#c8731c"/><path d="M1.5 3.5L8 9l6.5-5.5" stroke="#fff" stroke-width="1.3" fill="none"/></svg>
        maren@tidementoring.com.au
      </li>
      <li>
        <svg viewBox="0 0 16 16"><circle cx="8" cy="8" r="6.5" fill="none" stroke="#c8731c" stroke-width="1.5"/><ellipse cx="8" cy="8" rx="2.8" ry="6.5" fill="none" stroke="#c8731c" stroke-width="1.2"/><path d="M1.5 8h13" stroke="#c8731c" stroke-width="1.2"/></svg>
        www.tidementoring.com.au
      </li>
      <li>
        <span class="social-dots"><span></span><span></span><span></span></span>
        @tidementoringAU
      </li>
    </ul>

    <p class="strapline">A thinking partner to help you cut through the noise</p>
    <div class="front__edge"></div>
  </section>

  <section class="card card--back" aria-label="Card back">
    <div class="back__photo" role="img" aria-label="Photo of sunlit grass with soft glowing sunshine"></div>
    <div class="brand back__brand"><span class="brand__dot"></span>Tide Mentoring</div>
  </section>
</body>
</html>
```